logo & Business Card Design

NovaGuard Termite & Pest Control, I need a great logo, take my ideas and run with them!
I will use this in marketing and website so needs to be eye catching but professional

Target Market(s)

Resedintial & Business

Industry/Entity Type

Marketing

Contact Information for Business Card

Need front side with pertinent info & Logo; back side will have a 25% off initial services Coupon!

Font styles to use
Sans Serif

Colors
ec1f27
1b1b1b

Requirements
Must have
• Professional logo and style
Nice to have
• Raised lettering, black, red, white colors maybe? I'm flexible, but those colors go good on any background, vehicle, uniform, etc...
Should not have
• Cheesy

```html
<!DOCTYPE html>
<html lang="en">
<head>
<meta charset="utf-8">
<title>NovaGuard Termite &amp; Pest Control – Business Card</title>
<link href="https://fonts.googleapis.com/css2?family=Open+Sans:wght@400;600;700&display=swap" rel="stylesheet">
<style>
  :root {
    --backdrop: #ececec;
    --card-white: #f7f7f7;
    --card-black: #1b1b1b;
    --card-black-edge: #2a2a2a;
    --ink: #1b1b1b;
    --ink-soft: #555555;
    --ink-muted: #6b6b6b;
    --accent-red: #ec1f27;
    --paper-light: #ffffff;
  }
  * { box-sizing: border-box; margin: 0; padding: 0; }
  html, body {
    width: 1200px;
    height: 900px;
    overflow: hidden;
    background: var(--backdrop);
    font-family: "Open Sans", sans-serif;
  }
  .canvas {
    position: relative;
    width: 1200px;
    height: 900px;
  }
  .card {
    position: absolute;
    width: 490px;
    height: 280px;
    border-radius: 3px;
    box-shadow: 0 10px 24px rgba(0,0,0,0.12);
  }

  /* Front: contact side */
  .card-front {
    left: 90px;
    top: 450px;
    background: var(--card-white);
    color: var(--ink);
    padding: 34px 36px;
  }
  .person-name {
    font-size: 22px;
    font-weight: 700;
    color: var(--ink);
    line-height: 1.15;
  }
  .person-role {
    font-size: 14px;
    font-weight: 400;
    color: var(--ink-muted);
    margin-bottom: 26px;
  }
  .contact-list {
    list-style: none;
    font-size: 14px;
    line-height: 1.25;
  }
  .contact-label {
    color: var(--ink);
    font-weight: 600;
  }
  .contact-value {
    color: var(--ink-soft);
  }
  .front-brand {
    position: absolute;
    right: 32px;
    bottom: 40px;
    display: flex;
    align-items: center;
    gap: 10px;
  }
  .brand-mark {
    width: 14px;
    height: 14px;
    background: var(--accent-red);
  }
  .brand-name {
    font-size: 24px;
    font-weight: 700;
    color: var(--ink);
  }

  /* Back: brand side */
  .card-back {
    left: 620px;
    top: 170px;
    background: radial-gradient(ellipse at 45% 40%, var(--card-black-edge), var(--card-black) 70%);
    color: var(--paper-light);
    display: flex;
    flex-direction: column;
    align-items: center;
    justify-content: center;
    gap: 16px;
  }
  .back-brand {
    display: flex;
    align-items: center;
    gap: 10px;
  }
  .back-brand .brand-name {
    color: var(--paper-light);
    font-size: 28px;
  }
  .tagline {
    font-size: 13px;
    font-weight: 400;
    color: var(--paper-light);
    letter-spacing: 0.2px;
  }
</style>
</head>
<body>
<main class="canvas">

  <section class="card card-back" aria-label="Business card, brand side">
    <div class="back-brand">
      <span class="brand-mark" aria-hidden="true"></span>
      <span class="brand-name">NovaGuard</span>
    </div>
    <p class="tagline">“A Shield of protection For Your Home or Business”</p>
  </section>

  <section class="card card-front" aria-label="Business card, contact side">
    <h1 class="person-name">Daniel Hart</h1>
    <p class="person-role">Managing Director</p>
    <ul class="contact-list">
      <li class="contact-label">telephone</li>
      <li class="contact-value">055-987 654 321</li>
      <li class="contact-label">email</li>
      <li class="contact-value">hello@novaguardpest.com</li>
      <li class="contact-label">address</li>
      <li class="contact-value">2345, adress goes here, country</li>
    </ul>
    <div class="front-brand">
      <span class="brand-mark" aria-hidden="true"></span>
      <span class="brand-name">NovaGuard</span>
    </div>
  </section>

</main>
</body>
</html>
```